Create a "germ free" Poster Design Project

Hi we're a media business who sells advertising space on a unique dispensing device that also sanitizes your hands.

I'm looking for a poster design that highlights the need to sanitize hands which removes 99.9% of germs and also promotes a healthy & clean lifestyle.
(you may want to use kid friendly images of bugs to highlight germs)
Whilst the primary message will be to sanitize your hands the secondary message is also to "use this space" to advertise on.

The poster should be colorful yet simple and not too wordy.

Thanks

Target Market(s)

General cunsumer public but more specifically women and moms

Industry/Entity Type

Advertising

Requirements
Must have
• A central picture (animated or real) to highlight the practice of sanitizing hands (or removing germs)
Perhaps an arrow down to invite consumers to "try it now, its free'
Nice to have
• Referal to our web site: Brelvona.com.au (currently not operational) and email info@brelvona.com.au
Perhaps an image of a baby's hand with a creative tag line.
Should not have
• Nothing too gross looking

```html
<!DOCTYPE html>
<html lang="en">
<head>
<meta charset="utf-8">
<title>Brelvona – Germ Free Poster</title>
<link rel="stylesheet" href="https://fonts.googleapis.com/css2?family=Ubuntu:wght@400;500;700&display=swap">
<style>
  :root {
    --backdrop: #e9e6e1;
    --paper: #f6f5f1;
    --ink: #3f3f3f;
    --ink-soft: #4a4a4a;
    --accent: #d8673f;
    --plum: #9c2a70;
    --plum-dark: #7a1b56;
    --plum-light: #b2408a;
    --cream: #fbf3e3;
    --rule: #d6d4cf;
  }
  * { box-sizing: border-box; margin: 0; padding: 0; }
  html, body {
    width: 1200px; height: 900px; overflow: hidden;
    background: var(--backdrop);
    font-family: "Ubuntu", "Helvetica Neue", Arial, sans-serif;
  }
  .poster {
    position: absolute; left: 320px; top: 45px;
    width: 560px; height: 805px;
    background: var(--paper);
    box-shadow: 0 2px 10px rgba(0,0,0,.18);
  }
  .brand {
    height: 103px;
    display: flex; align-items: center; justify-content: center; gap: 10px;
    border-bottom: 3px solid var(--rule);
    padding-top: 4px;
  }
  .brand-dot {
    width: 46px; height: 46px; border-radius: 50%;
    background: var(--plum);
  }
  .brand-name {
    font-size: 30px; font-weight: 700; color: var(--plum);
  }
  .headline {
    margin-top: 28px;
    text-align: center;
    font-size: 28px; font-weight: 700; color: var(--ink);
    line-height: 44px;
  }
  .headline .stat { font-size: 38px; color: var(--accent); }
  .offer {
    position: relative;
    margin: 20px auto 0; width: 526px; height: 130px;
  }
  .offer svg { position: absolute; inset: 0; }
  .offer-text {
    position: relative; text-align: center; color: var(--cream);
    padding-top: 12px; font-weight: 500;
  }
  .offer-lead { font-size: 30px; line-height: 38px; }
  .offer-main { font-size: 42px; font-weight: 700; line-height: 50px; }
  .advertise {
    margin-top: 30px; text-align: center;
    font-size: 22px; color: var(--ink-soft);
  }
  .contact-bar {
    position: absolute; left: 0; top: 388px; width: 560px; height: 34px;
    display: flex;
    background: linear-gradient(var(--plum-light), var(--plum-dark));
    color: #fff; font-weight: 700;
  }
  .contact-bar span {
    display: flex; align-items: center; justify-content: center;
  }
  .contact-web { width: 280px; font-size: 19px; border-right: 1px solid rgba(0,0,0,.3); }
  .contact-mail { flex: 1; font-size: 16px; }
  .hero {
    position: absolute; left: 0; top: 422px; width: 560px; height: 331px;
    background: linear-gradient(135deg, #d7dadb 0%, #a9adaf 45%, #6f7476 100%);
  }
  .tagline {
    position: absolute; left: 0; top: 753px; width: 560px; height: 52px;
    display: flex; align-items: center; justify-content: center;
    font-size: 34px; font-weight: 700; color: var(--ink);
  }
  .tagline em { font-style: normal; color: var(--accent); }
</style>
</head>
<body>
  <main class="poster">
    <header class="brand">
      <span class="brand-dot"></span>
      <span class="brand-name">Brelvona</span>
    </header>

    <h1 class="headline">Use Sanitizer. Kill <span class="stat">99.9%</span> Germs.</h1>

    <div class="offer">
      <svg width="526" height="130" viewBox="0 0 526 130" aria-hidden="true">
        <defs>
          <linearGradient id="offerFill" x1="0" y1="0" x2="0" y2="1">
            <stop offset="0" stop-color="#b5438d"/>
            <stop offset="1" stop-color="#7c1c58"/>
          </linearGradient>
        </defs>
        <polygon points="4,0 522,0 526,4 526,96 296,96 263,130 230,96 0,96 0,4" fill="url(#offerFill)"/>
      </svg>
      <div class="offer-text">
        <p class="offer-lead">Try it NOW!</p>
        <p class="offer-main">It’s FREE!</p>
      </div>
    </div>

    <p class="advertise">Use This Space To Advertise.</p>

    <div class="contact-bar">
      <span class="contact-web">Brelvona.com.au</span>
      <span class="contact-mail">info@brelvona.com.au</span>
    </div>

    <div class="hero" role="img" aria-label="Photo of a young child washing hands at a kitchen sink, with a cartoon germ character in an orange burst speech bubble"></div>

    <p class="tagline">Be&nbsp;<em>Aware</em>, Wash with&nbsp;<em>Care</em>!</p>
  </main>
</body>
</html>
```